One page website

I'm looking for a landing page for my company. Just a brief description of our medical device technology with some images

Coding

Coded - Design and coding required

```html
<!DOCTYPE html>
<html lang="en">
<head>
<meta charset="utf-8">
<title>Veritas Spine — Solving Children's Scoliosis</title>
<link rel="stylesheet" href="https://fonts.googleapis.com/css2?family=Nunito:wght@600;700;800&family=Roboto:wght@300;400;500&display=swap">
<style>
:root{
  --ink:#1d2833;
  --text:#5b6670;
  --muted:#8a949c;
  --blue:#2b9fd9;
  --blue-light:#a9d7ef;
  --blue-pale:#e9f3f9;
  --green:#8cc63f;
  --red:#d7262b;
  --dark:#3b4452;
  --line:#d6dee4;
  --white:#ffffff;
}
*{box-sizing:border-box;margin:0;padding:0}
html,body{width:1200px;height:5199px;overflow:hidden}
body{font-family:"Roboto",sans-serif;color:var(--text);background:var(--white);position:relative}
section,header,footer{position:absolute;left:0;width:1200px;overflow:hidden}
.abs{position:absolute}
h1,h2{font-family:"Nunito",sans-serif;color:var(--ink)}
h2{font-size:26px;font-weight:800;text-align:center}
.divider{display:flex;align-items:center;justify-content:center;gap:8px;margin-top:14px}
.divider span{width:28px;height:2px;background:var(--ink);opacity:.7}
.divider i{width:8px;height:8px;border-radius:50%;background:var(--green)}
.btn{display:flex;align-items:center;justify-content:center;background:var(--blue);color:var(--white);font-size:15px;letter-spacing:.5px;border-right:7px solid var(--green);text-transform:uppercase}
.btn-outline{display:flex;align-items:center;justify-content:center;border:2px solid var(--blue);border-right:5px solid var(--green);color:var(--blue);font-size:10px;text-transform:uppercase;background:var(--white)}
.photo{position:absolute}
.brand{display:flex;align-items:center;gap:8px;font-family:"Roboto",sans-serif;font-weight:400;color:var(--green)}
.brand .mark{width:12px;height:12px;border-radius:50%;background:var(--green)}

/* header / hero */
.hero{top:0;height:600px;background:linear-gradient(90deg,#e8f2f9 0%,#deedf7 45%,#d3e6f2 100%)}
.hero .photo{left:560px;top:0;width:640px;height:600px;background:linear-gradient(110deg,rgba(222,237,247,0) 0%,#e7eef0 30%,#d9e2e2 60%,#c7d5dc 100%)}
.hero .brand{left:100px;top:55px;font-size:22px}
.nav{left:440px;top:32px;display:flex;gap:36px;font-size:15px;color:var(--ink);align-items:center}
.nav .btn-outline{width:162px;height:44px;font-size:15px;margin-left:0}
.hero h1{left:234px;top:146px;font-size:52px;line-height:60px;font-weight:800}
.hero .lead{left:236px;top:341px;font-size:16px;color:var(--ink)}
.hero .lead em{font-style:normal;color:var(--blue)}
.hero .btn{left:236px;top:403px;width:178px;height:50px}

/* mission */
.mission{top:600px;height:616px;background:linear-gradient(90deg,#f3f7fa,#e6f0f7)}
.mission .photo{left:0;top:0;width:665px;height:616px;background:linear-gradient(100deg,#d7c2b0 0%,#e8ecef 40%,#f1f5f8 75%,rgba(241,245,248,0) 100%)}
.mission h2{position:absolute;left:523px;top:62px;font-size:26px;text-align:left}
.mission .divider{position:absolute;left:555px;top:100px;margin:0}
.mission .intro{left:676px;top:160px;width:410px;font-size:21px;line-height:31px;color:var(--text)}
.mission h3{position:absolute;left:676px;top:320px;font-family:"Roboto",sans-serif;font-weight:500;font-size:17px;color:var(--ink)}
.checks{left:672px;top:358px;width:430px;list-style:none}
.checks li{display:flex;gap:14px;font-size:14px;line-height:22px;margin-bottom:12px}
.checks svg{flex:none;width:18px;height:18px;margin-top:2px}

/* problems */
.problems{top:1216px;height:644px;background:var(--white)}
.problems h2{position:absolute;left:0;width:1200px;top:70px}
.problems .divider{position:absolute;left:0;width:1200px;top:112px;margin:0}
.option{position:absolute;top:176px;width:340px;text-align:center}
.option .mark-icon{width:54px;height:54px;margin:0 auto}
.option .photo{position:relative;width:142px;height:142px;border-radius:50%;border:3px solid var(--blue);margin:8px auto 0}
.option h3{font-family:"Roboto",sans-serif;font-weight:400;font-size:20px;color:var(--ink);margin-top:20px}
.option h3 small{font-size:7px;color:var(--blue);text-transform:uppercase;vertical-align:middle;margin-left:4px}
.option p{font-size:16px;line-height:28px;color:var(--text);margin-top:2px}

/* banner */
.banner{top:1860px;height:258px;background:linear-gradient(90deg,#3a4351,#48525f 50%,#59636e)}
.banner p{position:absolute;left:300px;width:600px;top:56px;text-align:center;color:var(--white);font-size:18px;line-height:33px}
.banner .btn{left:510px;top:177px;width:178px;height:50px}

/* team */
.team{top:2118px;height:660px;background:var(--blue-pale)}
.team h2{position:absolute;left:0;width:1200px;top:66px}
.team .divider{position:absolute;left:0;width:1200px;top:108px;margin:0}
.member{position:absolute;top:195px;width:216px;height:329px;background:var(--white);border:1px solid var(--line);text-align:center;padding-top:20px}
.member .photo{position:relative;width:70px;height:70px;border-radius:50%;border:3px solid var(--green);margin:0 auto;background:linear-gradient(135deg,#c9d3da,#8d99a3)}
.member h3{font-family:"Roboto",sans-serif;font-weight:400;font-size:15px;color:var(--ink);margin-top:14px}
.member .role{font-size:10px;color:var(--muted);margin-top:2px;padding:0 6px}
.member p{font-size:12px;line-height:20px;margin-top:14px;padding:0 18px;color:var(--text)}
.member .social{position:absolute;left:0;right:0;bottom:38px;display:flex;justify-content:center;gap:22px}
.member .social i{width:12px;height:12px;background:var(--ink);border-radius:2px}
.team .btn-outline{position:absolute;left:545px;top:563px;width:111px;height:29px}

/* advantages */
.advantages{top:2778px;height:657px;background:linear-gradient(180deg,#b5dbf0,#a6d3ec)}
.advantages h2{position:absolute;left:0;width:1200px;top:70px}
.advantages .divider{position:absolute;left:0;width:1200px;top:112px;margin:0}
.adv-list{left:250px;top:226px;width:370px;list-style:none}
.adv-list li{position:relative;height:77px;padding:10px 0 0 72px}
.adv-list li.active{background:var(--white);width:361px}
.adv-list .num{position:absolute;left:12px;top:12px;width:42px;height:42px;border-radius:50%;background:var(--white);border:3px solid var(--blue-light);display:flex;align-items:center;justify-content:center;font-family:"Nunito",sans-serif;font-weight:800;font-size:22px;color:var(--ink)}
.adv-list li.active .num{background:var(--blue-light)}
.adv-list h3{font-family:"Roboto",sans-serif;font-weight:400;font-size:15px;color:var(--ink);text-transform:uppercase}
.adv-list p{font-size:12px;line-height:17px;color:var(--muted);width:230px}
.advantages .spine{left:726px;top:209px;width:371px;height:363px;background:linear-gradient(135deg,#3e4654,#56606c 50%,#c9b68e 75%,#3e4654)}
.advantages .device{left:658px;top:171px;width:119px;height:197px;background:linear-gradient(160deg,#2f3945,#dfe6ea 45%,#2b9fd9 80%);border:2px solid var(--white)}

/* comparison */
.comparison{top:3435px;height:815px;background:var(--white)}
.comparison h2{position:absolute;left:0;width:1200px;top:78px}
.comparison .divider{position:absolute;left:0;width:1200px;top:120px;margin:0}
table{position:absolute;left:234px;top:188px;width:730px;border-collapse:collapse;font-size:14px}
th{height:77px;background:var(--blue-light);color:var(--ink);font-weight:400;font-size:14px;border:1px solid #c5e2f2}
td{height:61px;border:1px solid var(--line);text-align:center;color:var(--muted);font-size:13px}
td:first-child{text-align:left;padding-left:20px;color:var(--ink);font-size:14px;width:214px}
td.ours{background:#f1f7fb}
td svg{width:34px;height:28px;vertical-align:middle}

/* contact */
.contact{top:4250px;height:598px;background:linear-gradient(90deg,#cfdbe2 0%,#e8eef2 35%,#f6f8fa 55%,#f8fafb 100%)}
.contact .photo{left:0;top:0;width:640px;height:598px;background:linear-gradient(100deg,#b7c9d6 0%,#d7dfe3 40%,rgba(246,248,250,0) 100%)}
.contact h2{position:absolute;left:0;width:1200px;top:78px}
.contact .divider{position:absolute;left:0;width:1200px;top:120px;margin:0}
.field{position:absolute;left:609px;width:368px;height:38px;background:var(--white);border:1px solid var(--line);display:flex;align-items:center;gap:12px;padding-left:14px;font-size:12px;color:var(--muted)}
.field i{width:10px;height:10px;background:var(--muted);border-radius:2px}
.field.message{align-items:flex-start;padding-top:12px;height:168px}
.contact .btn-outline{position:absolute;left:867px;top:551px;width:110px;height:27px}

/* footer */
footer{top:4848px;height:351px;background:var(--blue-light)}
footer .brand{position:absolute;left:232px;top:140px;font-size:30px}
.socials{position:absolute;left:234px;top:218px;display:flex;gap:19px}
.socials i{width:33px;height:33px;border-radius:50%;background:var(--ink)}
footer h3{position:absolute;font-family:"Roboto",sans-serif;font-weight:500;font-size:16px;color:var(--ink);top:72px}
.links{left:510px;top:110px;list-style:none;font-size:13px;line-height:24px;color:var(--ink)}
.contact-list{left:795px;top:110px;list-style:none;font-size:13px;color:var(--ink)}
.contact-list li{display:flex;gap:14px;margin-bottom:20px;line-height:24px}
.contact-list svg{width:18px;height:18px;margin-top:3px;flex:none}
</style>
</head>
<body>
<svg width="0" height="0" style="position:absolute">
  <defs>
    <symbol id="tick" viewBox="0 0 40 32"><path d="M3 17 L15 28 L37 4" fill="none" stroke="#8cc63f" stroke-width="6" stroke-linecap="round" stroke-linejoin="round"/></symbol>
    <symbol id="cross" viewBox="0 0 40 40"><path d="M6 6 L34 34 M34 6 L6 34" stroke="#d7262b" stroke-width="8" stroke-linecap="round"/></symbol>
  </defs>
</svg>

<header class="hero">
  <div class="photo" role="img" aria-label="Smiling young girl with a scoliosis patient in a bright clinic"></div>
  <div class="brand abs"><span class="mark"></span>Veritas Spine</div>
  <nav class="nav abs">
    <span>HOME</span><span>ABOUT</span><span>MISSION</span><span>SOLUTION</span><span>BENEFITS</span>
    <span class="btn-outline">Contact</span>
  </nav>
  <h1 class="abs">Solving<br>Children’s<br>Scoliosis</h1>
  <p class="lead abs">Btetter <em>Option</em> Fusion &amp; Bracing</p>
  <a class="btn abs">Contact</a>
</header>

<section class="mission">
  <div class="photo" role="img" aria-label="Doctor with a clipboard beside a mother and daughter"></div>
  <h2>Our Mission</h2>
  <div class="divider"><span></span><i></i><span></span></div>
  <p class="intro abs">Develop novel technologies focusing on non-fusion scoliosis correction allowing for non-surgical dynamic adjustment of implants over time.</p>
  <h3>ACCOMPLISHMENTS TO DATE</h3>
  <ul class="checks abs">
    <li><svg><use href="#tick"/></svg>Successful completion of pilot animal trial</li>
    <li><svg><use href="#tick"/></svg>Fully functional system validated in vivo for 10 weeks with no clinical complications</li>
    <li><svg><use href="#tick"/></svg>Positive dialogue with FDA on regulatory strategy, given recent Orthane approval</li>
    <li><svg><use href="#tick"/></svg>Winner of “Pediatric Device Pitch Challenge!”</li>
  </ul>
</section>

<section class="problems">
  <h2>Ptoblems and best solution</h2>
  <div class="divider"><span></span><i></i><span></span></div>
  <div class="option" style="left:86px">
    <svg class="mark-icon"><use href="#cross"/></svg>
    <div class="photo" role="img" aria-label="Child wearing a white back brace" style="background:linear-gradient(135deg,#e7e2de,#7a3440)"></div>
    <h3>BRACING</h3>
    <p>Poor Compliance (50%)<br>Rarely straighten spine<br>Multi-year treatment</p>
  </div>
  <div class="option" style="left:381px">
    <svg class="mark-icon"><use href="#cross"/></svg>
    <div class="photo" role="img" aria-label="X-ray of a spine fused with rods" style="background:radial-gradient(circle,#b7bcc0,#2b3036)"></div>
    <h3>FUSION</h3>
    <p>4+ hour surgery<br>Fusion is irreversible<br>Complications, infections, failures<br>Limiting motion for life</p>
  </div>
  <div class="option" style="left:724px">
    <svg class="mark-icon"><use href="#tick"/></svg>
    <div class="photo" role="img" aria-label="Spine model with a flexible vertebral tether" style="background:linear-gradient(135deg,#f1ede4,#d6c39a 60%,#e9edf0)"></div>
    <h3>VBT<small>non-fusion</small></h3>
    <p>66% Cost Savings<br>50% Saving in Surgery Time<br>50% Saving in Hospital Stay<br>Confirmed improved self-confidence</p>
  </div>
</section>

<section class="banner">
  <p>Between the Lakeside Children's group and Dr. Amari at Northbay University Medical Center (NUMC), 350+ VBT procedures were completed.1</p>
  <a class="btn abs">Contact</a>
</section>

<section class="team">
  <h2>Founding Team</h2>
  <div class="divider"><span></span><i></i><span></span></div>
  <div class="member" style="left:139px">
    <div class="photo" role="img" aria-label="Portrait of the founder"></div>
    <h3>JONAH BARROW</h3>
    <div class="role">Founder and CEO</div>
    <p>Co-founder and CEO of Spinara Labs. Acquired by Corvant in 2014. Leadership positions at Halden Labs and Brexter</p>
    <div class="social"><i></i><i></i><i></i></div>
  </div>
  <div class="member" style="left:375px">
    <div class="photo" role="img" aria-label="Portrait of the senior engineer"></div>
    <h3>DEVIN KOWAL</h3>
    <div class="role">Co-founder and Senior R&amp;D Engineer</div>
    <p>Senior R&amp;D engineer at Northbay State University, Westbridge</p>
    <div class="social"><i></i><i></i><i></i></div>
  </div>
  <div class="member" style="left:609px">
    <div class="photo" role="img" aria-label="Portrait of the VP of R&amp;D"></div>
    <h3>JOEL ASHFORD</h3>
    <div class="role">Co-Founder VP R&amp;D and Operations</div>
    <p>Previous Chief Science Officer at Spinara Labs. Previous leadership positions at Lumbera, Corvant and Halden Ortho</p>
    <div class="social"><i></i><i></i><i></i></div>
  </div>
  <div class="member" style="left:843px">
    <div class="photo" role="img" aria-label="Portrait of the chief science officer"></div>
    <h3>MOHAN KADIR PH.D</h3>
    <div class="role">Co-Founder Chief Science Officer</div>
    <p>Previous Chief Science Officer at Spinara Labs. Previous leadership positions at Lumbera, Corvant and Halden Ortho</p>
    <div class="social"><i></i><i></i><i></i></div>
  </div>
  <a class="btn-outline">See other</a>
</section>

<section class="advantages">
  <h2>Advantages of VBT</h2>
  <div class="divider"><span></span><i></i><span></span></div>
  <ol class="adv-list abs">
    <li><span class="num">1</span><h3>Continued skeletal growth</h3><p>Lorem ipsu m dolor sit amet, consec tetur adi.</p></li>
    <li class="active"><span class="num">2</span><h3>Partial motion preservation</h3><p>Lorem ipsu m dolor sit amet, consec tetur adi.</p></li>
    <li><span class="num">3</span><h3>Single treatment event</h3><p>Lorem ipsu m dolor sit amet, consec tetur adi.</p></li>
    <li><span class="num">4</span><h3>Little impact on activity</h3><p>Lorem ipsu m dolor sit amet, consec tetur adi.</p></li>
  </ol>
  <div class="spine abs" role="img" aria-label="3D rendering of a spine with a vertebral body tether"></div>
  <div class="device abs" role="img" aria-label="Handheld adjustment device"></div>
</section>

<section class="comparison">
  <h2>Comparison with other treatments</h2>
  <div class="divider"><span></span><i></i><span></span></div>
  <table>
    <thead><tr><th></th><th>VBT - VERITAS</th><th>VBT - ORTHANE</th><th>FUSION</th><th>BRACING</th></tr></thead>
    <tbody>
      <tr><td>FDA APPROVED</td><td class="ours"></td><td><svg><use href="#tick"/></svg></td><td><svg><use href="#tick"/></svg></td><td><svg><use href="#tick"/></svg></td></tr>
      <tr><td>OVER-CORRECTION<br>MANAGEMENT</td><td class="ours"><svg><use href="#tick"/></svg></td><td></td><td>N/A</td><td>N/A</td></tr>
      <tr><td>TETHER CAN BREAK<br>UNDER PRESSURE</td><td class="ours">NO</td><td>YES</td><td>N/A</td><td>N/A</td></tr>
      <tr><td>MINIMALLY INVASIVE<br>SURGERY</td><td class="ours"><svg><use href="#tick"/></svg></td><td><svg><use href="#tick"/></svg></td><td></td><td>N/A</td></tr>
      <tr><td>FULL SPINAL MOTION</td><td class="ours"><svg><use href="#tick"/></svg></td><td><svg><use href="#tick"/></svg></td><td></td><td></td></tr>
      <tr><td>BLOOD LOSS</td><td class="ours">LOW</td><td>LOW</td><td>HIGH</td><td>N/A</td></tr>
      <tr><td>RECOVERY TIME1,2</td><td class="ours">6 WEEKS</td><td>6 WEEKS</td><td>12 WEEKS</td><td>N/A</td></tr>
      <tr><td>MUSCLE SPARING</td><td class="ours"><svg><use href="#tick"/></svg></td><td><svg><use href="#tick"/></svg></td><td></td><td>N/A</td></tr>
    </tbody>
  </table>
</section>

<section class="contact">
  <div class="photo" role="img" aria-label="Young patient resting in a hospital bed"></div>
  <h2>Comparison with other treatments</h2>
  <div class="divider"><span></span><i></i><span></span></div>
  <div class="field" style="top:163px"><i></i>Your Name</div>
  <div class="field" style="top:228px"><i></i>Your Email</div>
  <div class="field" style="top:291px"><i></i>Your Phone</div>
  <div class="field message" style="top:353px"><i></i>Your Message</div>
  <a class="btn-outline">Submit</a>
</section>

<footer>
  <div class="brand"><span class="mark"></span>Veritas Spine</div>
  <div class="socials"><i></i><i></i><i></i></div>
  <h3 style="left:510px">QUICK LINKS</h3>
  <ul class="links abs">
    <li>Home</li><li>About &amp; Missions</li><li>Accomplishments</li><li>VBT Benefits</li><li>Blog</li><li>Contact</li>
  </ul>
  <h3 style="left:821px">CONTACT US</h3>
  <ul class="contact-list abs">
    <li><svg viewBox="0 0 24 24"><path d="M12 2a7 7 0 0 0-7 7c0 5 7 13 7 13s7-8 7-13a7 7 0 0 0-7-7zm0 9.5A2.5 2.5 0 1 1 12 6.5a2.5 2.5 0 0 1 0 5z" fill="#1d2833"/></svg>Alder Lane, 412, Millbrook</li>
    <li><svg viewBox="0 0 24 24"><path d="M2 5h20v14H2z" fill="#1d2833"/><path d="M2 5l10 8 10-8" fill="none" stroke="#a9d7ef" stroke-width="2"/></svg>hello@veritasspine.com</li>
    <li><svg viewBox="0 0 24 24"><path d="M6.6 10.8a15 15 0 0 0 6.6 6.6l2.2-2.2a1 1 0 0 1 1-.25 11.4 11.4 0 0 0 3.6.6 1 1 0 0 1 1 1V20a1 1 0 0 1-1 1A17 17 0 0 1 3 4a1 1 0 0 1 1-1h3.5a1 1 0 0 1 1 1 11.4 11.4 0 0 0 .6 3.6 1 1 0 0 1-.25 1z" fill="#1d2833"/></svg>01-555-204-317<br>01-555-204-318</li>
  </ul>
</footer>
</body>
</html>
```